Web Design Project

Looking for a stunning, eye catching website landing page for my online shopping mall.
a global shopping mall landing page which will act as a door way to:

1. For shoppers giving them links including:
a. Go shopping,
b. Shopping Community,
c. Search by location/country,
d. Search by category.
e. Register/Login
f. Mall Rewards & Benefits
Ideally set out using nice images for each search option.

2. For sellers/merchant including:
a. Start selling

Created section in maybe column format for featured Listings like
3. Partners, Affiliates & Investors Section/Link
4. Advertise/Banners Space Sponsorships
5. Testimonials/Link
6. Special Offers/Promos

If all this can be captured in on when page opens without having to scroll down.

Landing page is for http://brightcartplaza.example/ http://brightcartharborview.example/ where you can can an idea of site colours

Target Market(s)

Online Shoppers, Online Merchants, Affiliates

Industry/Entity Type

Online Shopping

Requirements
Must have
• Footer background image with a buildings and maybe people representing a shopping mall... could be done in vector form matching brand colours.

Nice matching header in light colours providing white background for logo
Nice to have
• Section to place video or slide image widget

```html
<!DOCTYPE html>
<html lang="en">
<head>
<meta charset="utf-8">
<title>BrightCart – 24/7 Shopping Convenience</title>
<link rel="stylesheet" href="https://fonts.googleapis.com/css2?family=Open+Sans:wght@400;600;700&display=swap">
<style>
  :root{
    --gold:#c8903f;
    --gold-dark:#a8752c;
    --ink:#2b2b2b;
    --text:#3a3a3a;
    --muted:#8a8a8a;
    --cream:#fbf8f2;
    --panel:#f3f2ef;
    --red:#d63a22;
    --red-dark:#a8250f;
    --video:#1e1e1e;
    --icon:#6d7f99;
  }
  *{box-sizing:border-box;margin:0;padding:0}
  html,body{width:1200px;height:776px;overflow:hidden;background:#fff}
  body{font-family:"Open Sans",Arial,sans-serif;color:var(--text)}
  .page{position:relative;width:1200px;height:776px;overflow:hidden;background:#fff}

  .header{position:absolute;left:0;top:0;width:1200px;height:113px;background:linear-gradient(#f7f3ea,#fdfcf9)}
  .brand{position:absolute;left:46px;top:32px;font-size:38px;font-weight:700;color:var(--ink);letter-spacing:-1px;display:flex;align-items:center;gap:10px}
  .brand-mark{width:22px;height:22px;background:var(--gold);border-radius:50%}
  .divider-v{position:absolute;border-left:2px dotted #c9c1b3}
  .search{position:absolute;left:335px;top:28px;width:298px;height:35px;border:1px solid #ddd;border-radius:18px;background:#fff}
  .search-btn{position:absolute;right:-1px;top:-1px;width:88px;height:35px;border-radius:18px;background:linear-gradient(#d9a75a,var(--gold-dark));color:#fff;font-size:14px;display:flex;align-items:center;justify-content:center}
  .search-opts{position:absolute;left:336px;top:74px;font-size:12px;color:var(--muted);display:flex;gap:30px}
  .search-opts span::before{content:"";display:inline-block;width:8px;height:8px;border:1px solid #ccc;margin-right:7px;vertical-align:0}
  .nav{position:absolute;left:694px;top:49px;display:flex;gap:18px;font-size:13.5px;color:var(--ink)}
  .nav a::before,.list li::before{content:"";display:inline-block;border-left:7px solid var(--gold);border-top:4px solid transparent;border-bottom:4px solid transparent;margin-right:8px}
  .nav a{color:inherit;text-decoration:none}
  .login{position:absolute;left:1074px;top:42px;width:77px;height:29px;background:linear-gradient(#d9a75a,var(--gold-dark));color:#fff;font-size:14px;display:flex;align-items:center;justify-content:center;border-radius:2px}

  .hero-photo{position:absolute;left:45px;top:118px;width:350px;height:414px;background:radial-gradient(ellipse at 50% 45%,#f1d9b8 0%,#e8a89a 45%,#f3e1c0 75%,#fff 100%)}
  .hero-copy{position:absolute;left:415px;top:128px;width:350px}
  .hero-copy h1{font-size:34px;font-weight:400;color:var(--ink);line-height:1.1}
  .hero-copy h2{font-size:19px;font-weight:400;color:var(--gold);margin-top:4px}
  .hero-copy p{font-size:13.5px;line-height:18px;margin-top:14px;color:var(--ink)}
  .cta{position:absolute;left:451px;top:432px;width:233px;height:62px;border-radius:31px;background:linear-gradient(#ef5a3c,var(--red) 55%,var(--red-dark));box-shadow:0 6px 8px rgba(0,0,0,.15);color:#fff}
  .cta b{position:absolute;left:30px;top:10px;font-size:19px;font-weight:600}
  .cta small{position:absolute;left:30px;top:38px;font-size:9px;font-weight:700;letter-spacing:.5px}
  .cta svg{position:absolute;right:20px;top:14px}

  .video{position:absolute;left:844px;top:130px;width:308px;height:236px;border-radius:6px;background:linear-gradient(#2c2c2c,var(--video))}
  .video-bar{position:absolute;left:13px;bottom:14px;width:282px;height:22px;background:#333;border-radius:3px}
  .video-bar i{position:absolute;left:8px;top:9px;width:265px;height:5px;background:#888}
  .video-bar i::before{content:"";position:absolute;left:0;top:0;width:45px;height:5px;background:#fff}
  .follow{position:absolute;left:848px;top:410px;font-size:20px;color:var(--ink)}
  .follow span{color:var(--gold)}
  .social{position:absolute;left:849px;top:447px;display:flex;gap:8px}
  .social i{width:26px;height:26px;border-radius:4px;background:var(--icon)}

  .lower{position:absolute;left:20px;top:532px;width:1147px;height:180px;background:linear-gradient(#f1f0ed,#fafafa)}
  .col{position:absolute;top:556px}
  .col h3{font-size:20px;font-weight:400;color:var(--ink)}
  .list{list-style:none;margin-top:12px;font-size:14px;color:var(--ink)}
  .list li{height:27px}
  .testimonial{position:absolute;left:497px;top:590px;width:290px}
  .avatar{position:absolute;left:0;top:0;width:26px;height:27px;border:1px solid #ccc;background:#c9cfd8}
  .testimonial p{margin-left:37px;font-size:13.5px;line-height:17.5px;color:var(--ink)}
  .testimonial cite{display:block;margin:5px 0 0 37px;font-size:12px;font-style:normal;color:var(--gold)}
  .sponsors{position:absolute;left:850px;top:600px;display:flex;gap:22px;align-items:center}
  .sponsor{display:flex;align-items:center;gap:6px;font-size:13px;font-weight:600;color:var(--ink)}
  .sponsor i{width:12px;height:12px;background:var(--gold)}

  .skyline{position:absolute;left:0;top:704px;width:1200px;height:72px;background:linear-gradient(#d29d50,var(--gold))}
</style>
</head>
<body>
<div class="page">
  <header class="header">
    <div class="brand"><i class="brand-mark"></i>BrightCart</div>
    <div class="divider-v" style="left:305px;top:28px;height:60px"></div>
    <div class="search"><div class="search-btn">Search</div></div>
    <div class="search-opts"><span>by Location</span><span>by Category</span></div>
    <div class="divider-v" style="left:664px;top:28px;height:60px"></div>
    <nav class="nav"><a href="#">Go Shopping</a><a href="#">Shopping Community</a><a href="#">Register</a></nav>
    <div class="login">Login</div>
  </header>

  <div class="hero-photo" role="img" aria-label="Photo of a happy shopper holding gift boxes and shopping bags"></div>

  <section class="hero-copy">
    <h1>Shopping</h1>
    <h2>24/7 Shopping Convenience</h2>
    <p>Bringing you the very best in online shopping. At BrightCart you will soon be able to find almost anything you want at your fingertips without having to leave the comfort of your home. Save hours of driving time, hours of physically searching store after store to find what you can find with a few clicks online.</p>
    <p>We are offering you 24/7 shopping experience from some of your favorite local businesses. Enjoy the convenience and support local businesses.</p>
  </section>

  <a class="cta" href="#"><b>Go Shopping</b><small>BRIGHTCART</small>
    <svg width="34" height="34" viewBox="0 0 34 34"><circle cx="17" cy="17" r="16" fill="#f2ece6"/><circle cx="17" cy="17" r="11" fill="#8a2a1a"/><path d="M14 11l6 6-6 6" stroke="#fff" stroke-width="3" fill="none"/></svg>
  </a>

  <div class="divider-v" style="left:814px;top:130px;height:383px"></div>

  <div class="video">
    <svg style="position:absolute;left:144px;top:92px" width="22" height="28" viewBox="0 0 22 28"><path d="M0 0l22 14L0 28z" fill="#fff"/></svg>
    <div class="video-bar"><i></i></div>
  </div>

  <div class="follow">Follow Bright<span>Cart</span></div>
  <div class="social"><i></i><i></i><i></i><i></i><i></i><i></i><i></i></div>

  <div class="lower"></div>

  <div class="col" style="left:46px"><h3>Mall Opportunities</h3>
    <ul class="list"><li>Merchant Signup</li><li>Affiliate</li><li>Employment</li><li>Advertise</li></ul></div>
  <div class="col" style="left:305px"><h3>Partners</h3>
    <ul class="list"><li>Company 1</li><li>Company 2</li><li>Company 3</li></ul></div>
  <div class="col" style="left:497px"><h3>Testimonials</h3></div>
  <div class="testimonial"><div class="avatar"></div>
    <p>Lorem ipsum dolor sit amet, consect adipiscing elit, sed diam nonummy euismod tincidunt ut laoreet.</p>
    <cite>Mr. Harlow</cite></div>
  <div class="col" style="left:858px"><h3>Sponsorships</h3></div>
  <div class="sponsors">
    <div class="sponsor"><i></i>Fieldgreen</div>
    <div class="sponsor"><i></i>Maple Row</div>
    <div class="sponsor"><i></i>Orchard Tech</div>
  </div>

  <div class="skyline" role="img" aria-label="Golden city skyline of mall buildings along the footer"></div>
</div>
</body>
</html>
```